Brightline Tech Partners Website Design

I have here a website mockup. If you need anything further please feel free to reach out to me! Thank you!

Current site: http://brightlinetechpartners.example/

We want it clean, concise and eye catching.

Menu: I want the same idea we used from pellaroweb.example with the logo in the middle and in the menu:

Home, About Us, How Can We Help?, Media, Blog, Contact Us.

Let's have the Social Media icons at the very top please.

For the banner - we want a imagevault chess image sort of like imagevault photo 122579353 or 77865526

I want the words "Plan Ahead, Work Smarter, Stay Strong" to come in one at a time and then "Brightline Tech Partners" to show up on the banner.

Maybe have "Grow Your Business with Managed IT Services from Brightline Tech Partners" somewhere permanently on the banner that still suits everything.

Services Section: Maybe we can have them as chess pieces with something along the lines of "Make Your Next Move" - Managed IT Services, New Jersey Cloud Computing, Protect Your Business Data, Managed Email Solutions (Background 514558306)

Next Area: What sets us apart?/Testimonials (I want this as a split area) (Can we please use the banner image paralex here?)

(This is for the What Sets Us Apart side)
Outsmart threats before they reach your networks.

Outperform with the newest and latest technologies to not only keep you up and running, but to keep you at an advantage.

Outlast by embracing Business Continuity with Brightline Tech Partners by your side. (I will let you choose the background for here!)

Next Area: Book Your Free Two-Hour Review! (I want a form similar to the one on the old site.)

Next area: Blogs/Sign Up for our newsletter! (Again, please choose a relevant background)

Next Area:Contact Us area with service pages. I really like the contact us part in dorvaly.example where it shows the geographical area.

Target Market(s)

Business Owners in New Jersey looking to outsource their business IT, computer and network support.

Industry/Entity Type

Information Technology

Number of Pages Required

1 page

Font styles to use
Sans Serif

Requirements
Must have
• We want this website to be very sharp. I like bright colors, creative imagery.
• In the footer I must have @ 2016 Brightline Tech Partners | Privacy Policy | Sitemap
Should not have
• I am not a fan of stuffing everything in and making it very busy. I would like clean and professional

```html
<!DOCTYPE html>
<html lang="en">
<head>
<meta charset="utf-8">
<title>Brightline Tech Partners — Managed IT Services</title>
<link href="https://fonts.googleapis.com/css2?family=Lato:ital,wght@0,400;0,700;0,900;1,700&family=Open+Sans:wght@400;600;700&display=swap" rel="stylesheet">
<style>
:root{
  --frame:#e6e8ea;
  --blue:#4a9bd6;
  --blue-dark:#2f7fbf;
  --blue-light:#5aa8e0;
  --ink:#1f2328;
  --text:#3b3f44;
  --muted:#6a6f75;
  --white:#ffffff;
  --navy:#0d1a2b;
  --panel:#2c2e31;
  --footer:#d2d3d4;
  --hero-top:#7e94a6;
  --hero-mid:#aebfcc;
  --hero-low:#3f4d59;
}
*{box-sizing:border-box;margin:0;padding:0}
html,body{width:1200px;height:2699px;overflow:hidden}
body{background:var(--frame);font-family:"Open Sans",Arial,sans-serif;color:var(--text);position:relative}
.abs{position:absolute}
section{position:absolute;left:14px;width:1172px;overflow:hidden}

/* hero */
.hero{top:14px;height:751px}
.hero-photo{position:absolute;inset:0;background:linear-gradient(180deg,#d7dde2 0%,var(--hero-top) 18%,var(--hero-mid) 45%,#8fa2b1 62%,var(--hero-low) 88%,#2a333b 100%)}
.nav-rule{position:absolute;left:20px;right:20px;top:202px;height:2px;background:rgba(255,255,255,.55)}
.nav-item{position:absolute;top:82px;width:130px;text-align:center;color:var(--ink);font-family:"Lato",sans-serif;font-size:16px;letter-spacing:1px;text-transform:uppercase;line-height:1.15}
.nav-item.light{color:var(--white)}
.nav-item svg{display:block;margin:0 auto 10px;width:40px;height:40px}
.social{position:absolute;top:15px;right:20px;display:flex;gap:6px}
.social span{width:30px;height:30px;border-radius:50%;background:var(--blue)}
.brand-shield{position:absolute;left:436px;top:0;width:300px;height:240px}
.brand-name{position:absolute;left:436px;top:98px;width:300px;text-align:center;font-family:"Lato",sans-serif;font-weight:900;font-size:25px;color:var(--ink);line-height:1.15}
.hero-arrow{position:absolute;top:345px}
.hero-title{position:absolute;top:355px;left:0;width:100%;text-align:center;font-family:"Lato",sans-serif;font-weight:900;font-size:42px;letter-spacing:2px;color:var(--white);text-transform:uppercase;text-shadow:0 2px 6px rgba(0,0,0,.35)}
.hero-sub{position:absolute;top:416px;left:0;width:100%;text-align:center;font-family:"Lato",sans-serif;font-weight:700;font-size:21px;color:var(--white);text-shadow:0 1px 4px rgba(0,0,0,.4)}
.hero-sub em{font-style:normal;color:var(--blue-light)}

/* services */
.services{top:765px;height:203px;background:linear-gradient(180deg,#cfd3d6 0%,#e8eaec 40%,#f1f2f3 100%);overflow:visible}
.service{position:absolute;top:0;width:240px;text-align:center}
.service-badge{position:absolute;top:-50px;left:70px;width:100px;height:100px;border-radius:50%;background:var(--blue);border:6px solid #2d6fa3;box-shadow:0 3px 8px rgba(0,0,0,.35);display:flex;align-items:center;justify-content:center}
.service-badge .core{width:74px;height:74px;border-radius:50%;background:#e7eef4;display:flex;align-items:center;justify-content:center}
.service h3{margin-top:67px;font-family:"Lato",sans-serif;font-weight:700;font-size:17px;color:var(--blue-dark)}
.service p{margin-top:4px;font-size:13.5px;line-height:1.35;color:var(--text)}

/* split */
.split{top:968px;height:399px}
.split-bg{position:absolute;inset:0}
.split h2{position:absolute;top:55px;font-family:"Lato",sans-serif;font-weight:900;font-size:23px;color:var(--white);text-transform:uppercase;letter-spacing:.5px}
.split h2 em{font-style:normal;color:var(--blue-light)}
.split .testi-title{color:#111}
.split .testi-title em{color:var(--white)}
.point{position:absolute;left:40px;width:520px;display:flex;gap:18px;align-items:flex-start;color:var(--white);font-size:13px;line-height:1.5}
.point svg{flex:none;width:54px;height:48px}
.point p{padding-top:6px}
.btn{display:inline-block;background:var(--blue);color:var(--white);font-family:"Lato",sans-serif;font-weight:700;text-transform:uppercase;text-align:center;border-radius:3px}
.learn{position:absolute;left:223px;top:308px;width:141px;height:38px;line-height:38px;font-size:15px}
.quote-card{position:absolute;left:666px;top:112px;width:427px;height:149px;background:rgba(255,255,255,.9);border-radius:12px;padding:22px 70px 18px 58px;font-size:12.5px;line-height:1.5;color:var(--text)}
.quote-mark{position:absolute;font-family:"Lato",sans-serif;font-weight:900;font-size:54px;color:#333;line-height:1}
.avatar{position:absolute;left:971px;top:212px;width:96px;height:96px;border-radius:50%;background:linear-gradient(160deg,#c9b39a,#8a7866);border:4px solid var(--white)}
.reviewer{position:absolute;left:670px;top:281px;font-family:"Lato",sans-serif;font-style:italic;font-weight:700;font-size:17px;color:var(--white)}
.dots{position:absolute;left:840px;top:337px;display:flex;gap:5px}
.dots span{width:11px;height:11px;border-radius:50%;border:1.5px solid var(--white)}
.dots span:first-child{background:var(--white)}

/* call to action */
.cta{top:1367px;height:391px;background:linear-gradient(135deg,#f4f5f6 0%,#e7e9eb 45%,#f6f6f7 70%,#e4e6e8 100%)}
.cta-lead{position:absolute;left:63px;top:140px;font-family:"Lato",sans-serif;font-weight:700;font-size:22px;color:var(--ink)}
.cta-head{position:absolute;left:63px;top:170px;font-family:"Open Sans",sans-serif;font-weight:700;font-size:38px;color:var(--ink);letter-spacing:-.5px}
.cta-offer{position:absolute;left:63px;top:221px;font-family:"Open Sans",sans-serif;font-weight:700;font-size:34px;color:var(--blue);letter-spacing:-.5px}
.lead-form{position:absolute;left:770px;top:38px;width:340px;height:304px;background:var(--panel)}
.lead-form h4{height:42px;line-height:42px;background:var(--blue);color:var(--white);text-align:center;font-family:"Lato",sans-serif;font-weight:900;font-size:17px;text-transform:uppercase}
.field{position:absolute;height:34px;background:var(--white);border:1px solid #bbb;font-size:13px;color:#555;padding-left:12px;line-height:32px}
.submit{position:absolute;left:20px;top:238px;width:148px;height:34px;line-height:34px;font-size:15px;border-radius:0}

/* blog */
.blog{top:1758px;height:491px;background:radial-gradient(ellipse at 50% 30%,#1d3553 0%,var(--navy) 70%)}
.blog h2{position:absolute;top:52px;width:100%;text-align:center;font-family:"Lato",sans-serif;font-weight:900;font-size:23px;color:var(--white);text-transform:uppercase}
.blog h2 em{font-style:normal;color:var(--blue-light)}
.post{position:absolute;top:113px;width:270px;height:328px;background:linear-gradient(180deg,#ffffff,#e9e9e9);border:4px solid var(--white);box-shadow:0 2px 8px rgba(0,0,0,.4)}
.post-img{height:180px}
.post h5{margin:12px 10px 0;font-size:13.5px;font-weight:700;color:var(--ink)}
.post p{margin:0 10px;font-size:13px;line-height:1.35;color:var(--text)}
.post .btn{position:absolute;left:45px;bottom:16px;width:180px;height:42px;line-height:42px;font-size:15px}

/* newsletter */
.newsletter{top:2249px;height:129px;background:var(--white)}
.newsletter h3{position:absolute;left:157px;top:40px;font-family:"Lato",sans-serif;font-weight:900;font-size:27px;color:var(--ink);text-transform:uppercase}
.newsletter p{position:absolute;left:157px;top:74px;font-size:15px;font-weight:600;color:var(--ink)}
.email-input{position:absolute;left:603px;top:43px;width:383px;height:42px;background:#e5e6e7;font-size:16px;color:#333;padding-left:16px;line-height:42px}
.signup{position:absolute;left:995px;top:43px;width:143px;height:42px;line-height:42px;font-size:19px;border-radius:0}

/* footer */
.footer{top:2378px;height:270px;background:var(--footer)}
.footer-brand{position:absolute;left:70px;top:120px;display:flex;align-items:center;gap:12px;font-family:"Lato",sans-serif;font-weight:900;font-size:24px;color:var(--ink)}
.footer-brand span{width:30px;height:30px;border-radius:50%;background:var(--blue)}
.f-col{position:absolute;top:38px}
.f-col h6{font-size:15px;font-weight:700;color:var(--ink);padding-bottom:8px;border-bottom:1px solid #555;margin-bottom:22px}
.f-col ul{list-style:none;font-size:12.5px;font-weight:600;color:var(--ink);line-height:21px}
.contact-row{display:flex;gap:12px;align-items:flex-start;font-size:12.5px;font-weight:600;color:var(--ink);line-height:17px;margin-bottom:18px}
.contact-row svg{flex:none}
.follow li{display:flex;align-items:center;gap:12px;margin-bottom:4px}
.follow li::before{content:"";width:13px;height:13px;background:var(--blue)}
.copyright{top:2648px;height:33px;background:var(--blue);color:var(--white);text-align:center;font-size:10.5px;font-weight:700;line-height:33px;letter-spacing:.3px}
</style>
</head>
<body>

<section class="hero">
  <div class="hero-photo" role="img" aria-label="Photo of a chessboard with black and white pieces, a black knight toppling a white king, in cool blue-grey light"></div>
  <div class="nav-rule"></div>

  <div class="social" aria-label="Social media links"><span></span><span></span><span></span></div>

  <div class="nav-item" style="left:25px">
    <svg viewBox="0 0 40 40"><path d="M4 20 20 6l16 14h-5v14h-8v-9h-6v9H9V20z" fill="#222"/></svg>Home</div>
  <div class="nav-item" style="left:155px">
    <svg viewBox="0 0 40 40" fill="#fff"><circle cx="20" cy="12" r="5"/><circle cx="9" cy="15" r="4"/><circle cx="31" cy="15" r="4"/><path d="M12 30c0-6 4-10 8-10s8 4 8 10zM2 30c0-5 3-8 7-8 2 0 3 1 4 2-2 2-3 4-3 6zM38 30c0-5-3-8-7-8-2 0-3 1-4 2 2 2 3 4 3 6z"/></svg>About</div>
  <div class="nav-item" style="left:286px">
    <svg viewBox="0 0 40 40" fill="none" stroke="#fff" stroke-width="2"><rect x="8" y="6" width="22" height="28"/><path d="M13 13h12M13 19h12M13 25h8"/><circle cx="30" cy="9" r="5" fill="#fff"/></svg>How can<br>we help</div>
  <div class="nav-item light" style="left:754px">
    <svg viewBox="0 0 40 40" fill="none" stroke="#fff" stroke-width="2"><circle cx="20" cy="20" r="15"/><path d="M16 13l11 7-11 7z" fill="#fff"/></svg>Media</div>
  <div class="nav-item light" style="left:886px">
    <svg viewBox="0 0 40 40" fill="#fff"><rect x="7" y="6" width="6" height="5"/><rect x="15" y="6" width="18" height="5"/><rect x="7" y="14" width="6" height="5"/><rect x="15" y="14" width="18" height="5"/><rect x="7" y="22" width="6" height="5"/><rect x="15" y="22" width="18" height="5"/><rect x="7" y="30" width="6" height="5"/><rect x="15" y="30" width="18" height="5"/></svg>Blog</div>
  <div class="nav-item light" style="left:1026px">
    <svg viewBox="0 0 40 40" fill="none" stroke="#fff" stroke-width="2"><path d="M4 16l16-9 16 9v16H4z"/><path d="M4 16l16 11 16-11"/></svg>Contact</div>

  <svg class="brand-shield" viewBox="0 0 300 240" aria-hidden="true">
    <path d="M6 0h288v175L150 236 6 175z" fill="#4a9bd6"/>
    <path d="M16 0h268v167L150 224 16 167z" fill="#fbfcfd"/>
  </svg>
  <div class="brand-name">Brightline Tech<br>Partners</div>

  <svg class="hero-arrow" style="left:18px" width="30" height="90" viewBox="0 0 30 90"><path d="M28 2 2 45l26 43" fill="none" stroke="rgba(255,255,255,.6)" stroke-width="1.5"/></svg>
  <svg class="hero-arrow" style="right:18px" width="30" height="90" viewBox="0 0 30 90"><path d="M2 2l26 43L2 88" fill="none" stroke="rgba(255,255,255,.6)" stroke-width="1.5"/></svg>

  <h1 class="hero-title">Plan Ahead, Work Smarter, Stay Strong</h1>
  <p class="hero-sub">Grow Your Business with Managed IT Services from <em>Brightline Tech Partners</em></p>
</section>

<section class="services">
  <div class="service" style="left:82px">
    <div class="service-badge"><div class="core"><svg width="40" height="40" viewBox="0 0 40 40" fill="none" stroke="#2f7fbf" stroke-width="2"><rect x="12" y="5" width="16" height="28" rx="8"/><path d="M20 5v10"/></svg></div></div>
    <h3>Managed IT Services</h3>
    <p>Lorem ipsum dolor sit amet,<br>consectetuer adipiscing elit,<br>sed diam nonummy nibh euis<br>mod tincidunt ut laoreet dol.</p>
  </div>
  <div class="service" style="left:343px">
    <div class="service-badge"><div class="core"><svg width="44" height="40" viewBox="0 0 44 40" fill="none" stroke="#2f7fbf" stroke-width="2"><path d="M12 30H10a8 8 0 0 1 0-16 11 11 0 0 1 21-2 9 9 0 0 1 3 18h-2"/><path d="M22 34V18m-6 6 6-6 6 6"/></svg></div></div>
    <h3>New Jersey Cloud Computing</h3>
    <p>Lorem ipsum dolor sit amet,<br>consectetuer adipiscing elit,<br>sed diam nonummy nibh euis<br>mod tincidunt ut laoreet dol.</p>
  </div>
  <div class="service" style="left:602px">
    <div class="service-badge"><div class="core"><svg width="44" height="40" viewBox="0 0 44 40" fill="none" stroke="#2f7fbf" stroke-width="2"><rect x="4" y="7" width="32" height="24" rx="2"/><path d="M4 13h32"/><rect x="26" y="22" width="12" height="10" fill="#2f7fbf"/><path d="M28 22v-3a4 4 0 0 1 8 0v3"/></svg></div></div>
    <h3>Protect Your Business Data</h3>
    <p>Lorem ipsum dolor sit amet,<br>consectetuer adipiscing elit,<br>sed diam nonummy nibh euis<br>mod tincidunt ut laoreet dol.</p>
  </div>
  <div class="service" style="left:861px">
    <div class="service-badge"><div class="core"><svg width="44" height="40" viewBox="0 0 44 40" fill="none" stroke="#2f7fbf" stroke-width="2"><path d="M5 16 22 5l17 11v18H5z"/><path d="M5 16l17 11 17-11"/><circle cx="22" cy="15" r="4"/></svg></div></div>
    <h3>Managed Email Solutions</h3>
    <p>Lorem ipsum dolor sit amet,<br>consectetuer adipiscing elit,<br>sed diam nonummy nibh euis<br>mod tincidunt ut laoreet dol.</p>
  </div>
</section>

<section class="split">
  <svg class="split-bg" width="1172" height="399" viewBox="0 0 1172 399" preserveAspectRatio="none" role="img" aria-label="Dark technology photo on the left and a blue-tinted photo of a smiling business team on the right">
    <defs>
      <linearGradient id="darkSide" x1="0" y1="0" x2="1" y2="1"><stop offset="0" stop-color="#1a1f26"/><stop offset=".6" stop-color="#0c0f14"/><stop offset="1" stop-color="#22384d"/></linearGradient>
      <linearGradient id="blueSide" x1="0" y1="0" x2="1" y2="1"><stop offset="0" stop-color="#8cc0e6"/><stop offset=".5" stop-color="#5ea6dd"/><stop offset="1" stop-color="#4393d2"/></linearGradient>
    </defs>
    <rect width="1172" height="399" fill="url(#darkSide)"/>
    <polygon points="688,0 1172,0 1172,399 490,399" fill="url(#blueSide)"/>
  </svg>

  <h2 style="left:166px">What <em>sets us apart</em></h2>
  <div class="point" style="top:102px">
    <svg viewBox="0 0 54 48" fill="none" stroke="#4a9bd6" stroke-width="3"><circle cx="27" cy="24" r="19"/><path d="M18 24l7 7 13-14"/></svg>
    <p>Outsmart threats before they reach your networks.</p></div>
  <div class="point" style="top:163px">
    <svg viewBox="0 0 54 48" fill="none" stroke="#4a9bd6" stroke-width="3"><rect x="6" y="6" width="42" height="28" rx="2"/><path d="M20 44h14M27 34v10"/><path d="M14 26l8-8 6 5 10-10"/></svg>
    <p>Outperform with the newest and latest technologies to not only<br>keep you up and running, but to keep you at an advantage.</p></div>
  <div class="point" style="top:230px">
    <svg viewBox="0 0 54 48" fill="#4a9bd6"><path d="M4 22l10-8 10 6 6-4 20 6-8 10-10 6-10-4-8 2z"/></svg>
    <p>Outlast by embracing Business Continuity with Brightline Tech Partners<br>by your side.</p></div>
  <span class="btn learn">Learn more</span>

  <h2 class="testi-title" style="left:746px">Client <em>Testimonials</em></h2>
  <div class="quote-card">
    <span class="quote-mark" style="left:16px;top:16px">“</span>
    Lorem ipsum dolor sit amet, consectetu er adipiscing elit, sed diam nonummy nibh euismod tincidunt ut laoreet dolor magna aliquam erat volu. Wisi enim ad minim veniam.
    <span class="quote-mark" style="left:112px;top:95px">”</span>
  </div>
  <div class="avatar" role="img" aria-label="Portrait photo of the client"></div>
  <div class="reviewer">Daniel Marlowe</div>
  <div class="dots"><span></span><span></span><span></span><span></span></div>
</section>

<section class="cta">
  <p class="cta-lead">Tired Of Your Old IT Company Giving You The Run Around?</p>
  <p class="cta-head">Experience Brightline Tech Partners.</p>
  <p class="cta-offer">Book Your Free 2-Hour IT Review!</p>

  <form class="lead-form">
    <h4>Get started now!</h4>
    <div class="field" style="left:20px;top:75px;width:300px">Name</div>
    <div class="field" style="left:20px;top:115px;width:300px">Company</div>
    <div class="field" style="left:20px;top:155px;width:147px">Phone</div>
    <div class="field" style="left:173px;top:155px;width:147px">Email</div>
    <div class="field" style="left:20px;top:195px;width:300px">How Can We Help You?
      <svg style="position:absolute;right:10px;top:12px" width="12" height="8" viewBox="0 0 12 8"><path d="M1 1l5 5 5-5" fill="none" stroke="#333" stroke-width="2"/></svg></div>
    <span class="btn submit">Submit</span>
  </form>
</section>

<section class="blog">
  <h2>Latest <em>from blog</em></h2>
  <article class="post" style="left:31px">
    <div class="post-img" role="img" aria-label="Photo of colleagues meeting around a laptop" style="background:linear-gradient(135deg,#dfe6ee,#8fa3b8 60%,#4d5d6e)"></div>
    <h5>Blog #1</h5><p>Lorem ipsum dolor sit amet, consec tetuer adipiscing elit, sed diam.</p>
    <span class="btn">Read more</span></article>
  <article class="post" style="left:311px">
    <div class="post-img" role="img" aria-label="Photo of a glowing blue jigsaw puzzle with one piece lifted" style="background:radial-gradient(circle at 50% 50%,#bfe9f2,#2b8aa6 45%,#0c3448)"></div>
    <h5>Blog #2</h5><p>Lorem ipsum dolor sit amet, consec tetuer adipiscing elit, sed diam.</p>
    <span class="btn">Read more</span></article>
  <article class="post" style="left:591px">
    <div class="post-img" role="img" aria-label="Photo of a hand touching floating app icons on a dark blue background" style="background:linear-gradient(135deg,#0f2440,#2d5f95 55%,#112a48)"></div>
    <h5>Blog #3</h5><p>Lorem ipsum dolor sit amet, consec tetuer adipiscing elit, sed diam.</p>
    <span class="btn">Read more</span></article>
  <article class="post" style="left:871px">
    <div class="post-img" role="img" aria-label="Photo of blurred commuters walking through a bright glass hall" style="background:linear-gradient(180deg,#d9eef3,#7fbfce 55%,#3c7a8c)"></div>
    <h5>Blog #4</h5><p>Lorem ipsum dolor sit amet, consec tetuer adipiscing elit, sed diam.</p>
    <span class="btn">Read more</span></article>
</section>

<section class="newsletter">
  <svg class="abs" style="left:38px;top:34px" width="86" height="64" viewBox="0 0 86 64" fill="none" stroke="#2b2b2b" stroke-width="5" stroke-linejoin="round"><path d="M6 22 58 4l22 36-52 18z"/><path d="M6 22l40 12 12-30"/></svg>
  <h3>Subscribe to newsletter</h3>
  <p>Get a dose of inspiration delivered to your inbox daily.</p>
  <div class="email-input">Email Address</div>
  <span class="btn signup">Sign me up</span>
</section>

<section class="footer">
  <div class="footer-brand"><span></span>Brightline Tech Partners</div>

  <div class="f-col" style="left:445px;width:128px">
    <h6>Navigation</h6>
    <ul><li>Home</li><li>About</li><li>How Can We Help</li><li>Media</li><li>Blog</li><li>Contact</li></ul>
  </div>

  <div class="f-col" style="left:660px;width:228px">
    <h6>Contact Us</h6>
    <div class="contact-row">
      <svg width="22" height="22" viewBox="0 0 22 22" fill="none" stroke="#3d8fcc" stroke-width="2"><circle cx="11" cy="11" r="10"/><path d="M11 17s-4-4-4-7a4 4 0 0 1 8 0c0 3-4 7-4 7z"/></svg>
      <span>Brightline Tech Partners<br>48 Orchard Lane<br>Maple Ridge NJ 07990</span></div>
    <div class="contact-row">
      <svg width="22" height="22" viewBox="0 0 22 22" fill="none" stroke="#3d8fcc" stroke-width="2"><circle cx="11" cy="11" r="10"/><path d="M7 6l2 0 1 3-1.5 1a7 7 0 0 0 3.5 3.5l1-1.5 3 1v2c-5 1-10-4-9-9z" fill="#3d8fcc" stroke="none"/></svg>
      <span style="padding-top:2px">(555) 014-2290</span></div>
    <div class="contact-row">
      <svg width="22" height="22" viewBox="0 0 22 22" fill="none" stroke="#3d8fcc" stroke-width="2"><circle cx="11" cy="11" r="10"/><rect x="6" y="7.5" width="10" height="7" stroke-width="1.5"/><path d="M6 8l5 4 5-4" stroke-width="1.5"/></svg>
      <span style="padding-top:2px">hello@brightlinetech.example</span></div>
  </div>

  <div class="f-col follow" style="left:988px;width:98px">
    <h6>Follow Us</h6>
    <ul><li>Friendlink</li><li>Chirper</li><li>ProNet</li></ul>
  </div>
</section>

<section class="copyright">COPYRIGHT © 2016 BRIGHTLINE TECH PARTNERS. ALL RIGHTS RESERVED.</section>

</body>
</html>
```